Presentation Folder for dental clinic

We need a presentation folder design. The presentation folder is what we give to our patients with treatment plans, quotes, images, information sheets etc.
I have uploaded current stationary designs for assistance as well as a photo of our external sign design.
We are an upmarket dental clinic.
Professionalism and customer service is key to us.
We provide information in presentation folders to give to patients.
It needs to memorable and a statement to who we are.

Target Market(s)

Main patient base is Male and Female 40 years old to 70 years old

Industry/Entity Type

Dental Clinic

Font styles to use
Serif
Sans Serif

Requirements
Must have
• Design:
• -Professional
• -Timeless
• -Modern
• - Memorable
• - Statement (if a patient puts down the folder, it will be easily identifiable with as Corvel Dentals folder)
• Logo
• Address, phone, email, website
• Dr Leo Brandt name and degree details
• Colour scheme to match current logos and branding
• "Your Smile Our Passion" quote
Nice to have
• Services listed:
• - Sleep Dentistry
• - Happy Gas
• - Dental Implants
• - Cosmetic Dentistry
• - Oral Surgery
• - Alignora
• - Teeth Whitening
• - General Dentistry
• - Childrens Dentistry
• See website www.corveldental-example.com.au
Should not have
• Dental cliche photos

```html
<!DOCTYPE html>
<html lang="en">
<head>
<meta charset="utf-8">
<title>Corvel Dentals – Presentation Folder</title>
<link rel="stylesheet" href="https://fonts.googleapis.com/css2?family=Source+Sans+3:wght@400;600;700&display=swap">
<style>
  :root{
    --purple:#8a3f9f;
    --purple-mid:#b56fcb;
    --purple-soft:#dcb8e6;
    --purple-faint:#efe0f3;
    --grey-text:#8a8a8a;
    --grey-dark:#6b6b6b;
    --grey-band:#ececec;
    --grey-stripe:#f6f6f6;
    --white:#ffffff;
    --photo-a:#f3dccb;
    --photo-b:#e9cdb8;
  }
  *{box-sizing:border-box;margin:0;padding:0}
  html,body{width:1200px;height:847px;overflow:hidden;background:#f4eef5}
  body{font-family:"Source Sans 3",Arial,sans-serif;color:var(--grey-dark)}
  .folder-spread{display:flex;width:1200px;height:847px}
  .folder-page{position:relative;width:600px;height:847px;background:var(--white);overflow:hidden}
  .folder-page + .folder-page{border-left:1px solid #e2dbe4}
  .page-art{position:absolute;inset:0;width:600px;height:847px}

  /* back cover */
  .goal-headline{position:absolute;right:44px;top:44px;text-align:right;font-size:25px;line-height:1.1;color:var(--grey-text)}
  .goal-headline .accent{color:var(--purple)}
  .goal-headline strong{color:var(--purple);font-weight:700}
  .info-block{position:absolute;left:0;width:600px;text-align:center}
  .section-tab{display:inline-block;background:var(--purple);color:var(--white);font-size:11px;font-weight:700;letter-spacing:.5px;text-transform:uppercase;padding:4px 26px;border-radius:0 0 10px 10px}
  .info-row{font-size:12.5px;font-weight:600;color:var(--grey-text);margin-top:6px;display:flex;justify-content:center;gap:10px}
  .info-row .sep{color:var(--purple)}
  .services{top:452px}
  .hours{top:580px}
  .hours .info-row{gap:8px}
  .hours .day{color:var(--grey-dark)}
  .contact{top:706px}
  .contact .info-row{gap:14px;font-size:12.5px}
  .contact-address{position:absolute;left:36px;top:790px;display:flex;align-items:center;gap:8px;font-size:12.5px;font-weight:600;color:var(--grey-text)}
  .icon-dot{display:inline-flex;width:16px;height:16px;border-radius:50%;background:var(--purple);align-items:center;justify-content:center;vertical-align:middle;margin-right:5px}

  /* front cover */
  .doctor-details{position:absolute;right:40px;top:34px;font-size:9px;line-height:1.45;color:var(--grey-text);text-align:left}
  .doctor-details .doctor-name{color:var(--purple);font-weight:700;font-size:10.5px}
  .brand-name{position:absolute;left:0;right:0;top:580px;text-align:center;font-size:78px;font-weight:700;letter-spacing:-1px;color:var(--purple);line-height:1}
  .brand-tagline{position:absolute;left:0;right:0;top:680px;text-align:center;font-size:29px;color:var(--grey-text);letter-spacing:-.3px}
  .brand-tagline em{font-style:normal;color:var(--purple);font-weight:600}
</style>
</head>
<body>
<main class="folder-spread">

  <!-- Back cover -->
  <section class="folder-page back-cover">
    <svg class="page-art" viewBox="0 0 600 847" aria-hidden="false">
      <defs>
        <linearGradient id="backPhotoTone" x1="0" y1="0" x2="1" y2="1">
          <stop offset="0" stop-color="var(--photo-a)"/>
          <stop offset="1" stop-color="var(--photo-b)"/>
        </linearGradient>
      </defs>
      <rect x="0" y="16" width="600" height="5" fill="var(--purple)"/>
      <path d="M40,125 H455 C500,125 540,115 600,100 V150 C560,330 420,400 260,392 C150,386 70,345 0,312 V150 C10,135 25,125 40,125 Z"
            fill="url(#backPhotoTone)" role="img" aria-label="Photo of a smiling mother and daughter"/>
      <path d="M0,312 C70,345 150,386 260,392 C420,400 560,330 600,150 V185 C560,360 420,430 260,420 C150,414 70,375 0,342 Z" fill="var(--purple)"/>
      <path d="M0,342 C70,375 150,414 260,420 C420,430 560,360 600,185 V220 C560,390 420,455 260,446 C150,440 70,400 0,370 Z" fill="var(--purple-mid)"/>
      <path d="M0,370 C70,400 150,440 260,446 C420,455 560,390 600,220 V255 C560,420 420,478 260,470 C150,465 70,428 0,398 Z" fill="var(--purple-faint)"/>
      <rect x="0" y="482" width="600" height="72" fill="var(--grey-band)"/>
      <rect x="0" y="570" width="600" height="8" fill="var(--grey-stripe)"/>
      <rect x="0" y="600" width="600" height="48" fill="var(--grey-stripe)"/>
      <rect x="0" y="662" width="600" height="8" fill="var(--grey-band)"/>
      <rect x="0" y="762" width="600" height="85" fill="var(--grey-stripe)"/>
    </svg>

    <h2 class="goal-headline"><span class="accent">Our goal</span> is help you<br>show off your <strong>smile.</strong></h2>

    <div class="info-block services">
      <span class="section-tab">Services</span>
      <div class="info-row"><span>Sleep Dentistry</span><span class="sep">|</span><span>Happy Gas</span><span class="sep">|</span><span>Dental Implants</span><span class="sep">|</span><span>Cosmetic Dentistry</span></div>
      <div class="info-row"><span>Oral Surgery</span><span class="sep">|</span><span>Alignora</span><span class="sep">|</span><span>Teeth Whitening</span><span class="sep">|</span><span>General Dentistry</span><span class="sep">|</span><span>Childrens Dentistry</span></div>
    </div>

    <div class="info-block hours">
      <span class="section-tab">Opening Hours</span>
      <div class="info-row"><span class="day">Monday</span><span>9:00am – 5:00pm</span><span class="sep">|</span><span class="day">Tuesday</span><span>9:00am – 7:00pm</span><span class="sep">|</span><span class="day">Wednesday*</span><span>9:00am – 1:00pm</span></div>
      <div class="info-row"><span class="day">Thursday</span><span>9:00am – 5:00pm</span><span class="sep">|</span><span class="day">Friday</span><span>7:30am – 2:00pm</span></div>
    </div>

    <div class="info-block contact">
      <span class="section-tab">Contact Us</span>
      <div class="info-row"><span>info@corveldental-example.com.au</span><span>www.corveldental-example.com.au</span></div>
    </div>

    <div class="contact-address">
      <span><span class="icon-dot"><svg width="9" height="9" viewBox="0 0 10 10"><path d="M5,1 L9,5 H8 V9 H2 V5 H1 Z" fill="#fff"/></svg></span>214 Harbour Rd, Elwood, VIC, 3184.</span>
      <span style="margin-left:18px"><span class="icon-dot"><svg width="9" height="9" viewBox="0 0 10 10"><path d="M2,1 H4 L5,3.5 L3.8,4.5 C4.4,5.8 5.2,6.6 6.5,7.2 L7.5,6 L9,7 V9 C5,9 1,5 1,2 Z" fill="#fff"/></svg></span>03 9000 4417</span>
    </div>
  </section>

  <!-- Front cover -->
  <section class="folder-page front-cover">
    <svg class="page-art" viewBox="0 0 600 847">
      <defs>
        <linearGradient id="frontPhotoTone" x1="0" y1="0" x2="1" y2="1">
          <stop offset="0" stop-color="var(--photo-a)"/>
          <stop offset="1" stop-color="var(--photo-b)"/>
        </linearGradient>
      </defs>
      <rect x="0" y="16" width="600" height="5" fill="var(--purple)"/>
      <path d="M0,28 C200,20 430,60 600,200 V230 C430,95 200,55 0,62 Z" fill="var(--purple-soft)"/>
      <path d="M0,62 C200,55 430,95 600,230 V262 C430,130 200,92 0,96 Z" fill="var(--purple)"/>
      <path d="M0,96 C200,92 430,130 600,262 C520,400 380,470 250,462 C130,455 40,395 0,320 Z"
            fill="url(#frontPhotoTone)" role="img" aria-label="Photo of a mother and child brushing their teeth"/>
      <path d="M0,320 C40,395 130,455 250,462 C380,470 520,400 600,262 V300 C520,440 380,505 250,497 C130,490 40,430 0,358 Z" fill="var(--purple)"/>
      <path d="M0,358 C40,430 130,490 250,497 C380,505 520,440 600,300 V335 C520,470 380,530 250,523 C130,516 40,460 0,392 Z" fill="var(--purple-mid)"/>
      <path d="M0,392 C40,460 130,516 250,523 C380,530 520,470 600,335 V362 C520,495 380,552 250,546 C130,540 40,486 0,420 Z" fill="var(--purple-faint)"/>
    </svg>

    <div class="doctor-details">
      <div class="doctor-name">Dr Leo Brandt</div>
      <div>B.D.S. Northgate College</div>
      <div>Graduate Diploma in Clinical Dentistry</div>
      <div>(IV) Sedation &amp; Pain Control Eastbay University</div>
    </div>

    <h1 class="brand-name">Corvel Dental</h1>
    <p class="brand-tagline">Your <em>Smile</em> Our <em>Passion</em></p>
  </section>

</main>
</body>
</html>
```